rl ironcraft business card metallic look

revamp the existing design but want card to have a metalic look to it

Target Market(s)

construction industry

Industry/Entity Type

constrction

Contact Information for Business Card

front of card RL Ironcraft, phone 4163920857, email rl.ironcraftt@quellmail.example and instagram account; rl_ironcraft_

Font styles to use
Other font styles liked:
• masculine

Colors

Designer to choose only greyscale colors for use in the design.

Requirements
Must have
• back side RL Ironcraft then a list of everything : Siding, ACM Panels, Standing Seam,Soffit, Fascia, Gutters,Metal,Alu,inum, Viynyl, Metal Roofs and roof repairs
Nice to have
• I would like to keep the look of the existing card with the metal grids on the front
Should not have
• Need a design in two days

```html
<!DOCTYPE html>
<html lang="en">
<head>
<meta charset="utf-8">
<title>RL Ironcraft – Business Card</title>
<link href="https://fonts.googleapis.com/css2?family=Roboto+Condensed:wght@400;700&display=swap" rel="stylesheet">
<style>
  :root {
    --backdrop: #999999;
    --card: #2a2926;
    --name: #66655f;
    --ink: #f2f2f2;
    --steel-shadow: #1c1c1a;
    --steel-dark: #2f2e2b;
    --steel-mid: #4b4a46;
    --steel-light: #6e6c67;
    --steel-sheen: #85837d;
    --seam: #141413;
  }
  * { margin: 0; padding: 0; box-sizing: border-box; }
  html, body {
    width: 1200px; height: 1059px; overflow: hidden;
    background: var(--backdrop);
    font-family: "Roboto Condensed", "Arial Narrow", sans-serif;
  }
  .card {
    position: absolute; left: 256px;
    width: 714px; height: 408px;
    background: var(--card);
    overflow: hidden;
  }
  .card--front { top: 88px; }
  .card--back { top: 560px; }
  .card__art { position: absolute; inset: 0; width: 100%; height: 100%; }
  .brand-name {
    position: absolute; left: 0; right: 0; text-align: center;
    font-weight: 700; color: var(--name);
    text-transform: uppercase; letter-spacing: 0.05em; line-height: 1;
  }
  .card--front .brand-name { top: 128px; font-size: 64px; }
  .card--back .brand-name { top: 128px; font-size: 86px; }
  .contact {
    position: absolute; left: 0; right: 0; top: 260px;
    list-style: none; color: var(--ink);
    font-weight: 400; font-size: 23px;
    display: flex; flex-direction: column; align-items: center; gap: 15px;
  }
  .contact__item { display: flex; align-items: center; gap: 12px; line-height: 28px; }
  .contact__icon { width: 22px; height: 22px; flex: none; }
  .services {
    position: absolute; left: 30px; right: 30px; top: 312px;
    text-align: center; color: var(--ink);
    font-size: 22px; line-height: 30px;
  }
</style>
</head>
<body>

<section class="card card--front" aria-label="Card front">
  <svg class="card__art" viewBox="0 0 714 408">
    <defs>
      <linearGradient id="corrugated" x1="0" y1="0" x2="1" y2="0.6">
        <stop offset="0" stop-color="var(--steel-mid)"/>
        <stop offset="0.35" stop-color="var(--steel-light)"/>
        <stop offset="0.6" stop-color="var(--steel-dark)"/>
        <stop offset="1" stop-color="var(--steel-shadow)"/>
      </linearGradient>
      <linearGradient id="brushed" x1="0" y1="0" x2="1" y2="1">
        <stop offset="0" stop-color="var(--steel-mid)"/>
        <stop offset="0.45" stop-color="var(--steel-sheen)"/>
        <stop offset="1" stop-color="var(--steel-mid)"/>
      </linearGradient>
    </defs>
    <polygon role="img" aria-label="Corrugated metal panel texture" points="0,0 377,0 35,215 0,195" fill="url(#corrugated)"/>
    <polyline class="panel-seam" points="377,0 35,215 0,195" fill="none" stroke="var(--seam)" stroke-width="2"/>
    <polygon role="img" aria-label="Brushed steel plate texture" points="409,0 714,0 714,175" fill="url(#brushed)"/>
  </svg>

  <h1 class="brand-name">RL Ironcraft</h1>

  <ul class="contact">
    <li class="contact__item">
      <svg class="contact__icon" viewBox="0 0 24 24" aria-hidden="true">
        <path fill="#f2f2f2" d="M6.6 10.8a15.1 15.1 0 0 0 6.6 6.6l2.2-2.2a1 1 0 0 1 1-.25 11.4 11.4 0 0 0 3.6.57 1 1 0 0 1 1 1V20a1 1 0 0 1-1 1A17 17 0 0 1 3 4a1 1 0 0 1 1-1h3.5a1 1 0 0 1 1 1c0 1.25.2 2.45.57 3.57a1 1 0 0 1-.25 1z"/>
      </svg>
      <span>416-392-0857</span>
    </li>
    <li class="contact__item">
      <svg class="contact__icon" viewBox="0 0 24 24" aria-hidden="true">
        <rect x="2" y="5" width="20" height="14" fill="#f2f2f2"/>
        <path d="M2 5l10 8 10-8" fill="none" stroke="#2a2926" stroke-width="1.6"/>
      </svg>
      <span>rl.ironcraftt@quellmail.example</span>
    </li>
    <li class="contact__item">
      <svg class="contact__icon" viewBox="0 0 24 24" aria-hidden="true">
        <circle cx="12" cy="12" r="9" fill="none" stroke="#f2f2f2" stroke-width="2"/>
      </svg>
      <span>rl_ironcraft_</span>
    </li>
  </ul>
</section>

<section class="card card--back" aria-label="Card back">
  <h2 class="brand-name">RL Ironcraft</h2>
  <p class="services">Siding, ACM Panels, Standing Seam, Soffit, Fascia, Gutters, Metal,<br>Aluminum, Vinyl, Metal Roofs and Roofing Repairs</p>
</section>

</body>
</html>
```